Business Card Design for a Software Startup

We'd like to have a business card design. We already have a logo. Basically what we need is a clean design with name, address, cellphone and phone numbers, e-mail and web site address (front) and a space on the back with our logo with the company name on the right side and some texts on the bottom.
We are a development and consulting company in Brazil with highly qualified team of professionals in Java, iOS and Android development and consulting.

Target Market(s)

CIO, IT managers of mid to big size companies

Industry/Entity Type

Business

```html
<!DOCTYPE html>
<html lang="en">
<head>
<meta charset="utf-8">
<title>ZAVRIQ Business Card</title>
<link href="https://fonts.googleapis.com/css2?family=Source+Sans+3:wght@400;600;700&display=swap" rel="stylesheet">
<style>
  :root {
    --cyan: #00aeef;
    --indigo: #3f416d;
    --navy: #283d63;
    --white: #ffffff;
    --frame-grey: #8a8a8a;
    --frame-cyan: #9fd8ee;
    --brand-gradient: linear-gradient(90deg, var(--cyan) 0%, #1a86c0 40%, #2f5a8c 72%, var(--indigo) 100%);
  }
  * { margin: 0; padding: 0; box-sizing: border-box; }
  html, body {
    width: 1200px;
    height: 849px;
    overflow: hidden;
    background: var(--white);
    font-family: "Source Sans 3", sans-serif;
  }
  .canvas { position: relative; width: 1200px; height: 849px; }

  .card { position: absolute; background: var(--white); overflow: hidden; }

  /* Back side */
  .card--back {
    left: 222px; top: 47px; width: 646px; height: 353px;
    border: 1px solid var(--frame-grey);
  }
  .card--back .brand {
    position: absolute; left: 66px; top: 101px;
    display: flex; align-items: center; gap: 22px;
  }
  .brand-square {
    width: 103px; height: 103px; border-radius: 14px;
    background: var(--navy);
  }
  .card--back .brand-name {
    font-size: 104px; font-weight: 700; color: var(--navy);
    line-height: 1; letter-spacing: 5px; white-space: nowrap;
  }
  .tagline-band {
    position: absolute; left: 0; bottom: 0; width: 100%; height: 55px;
    background: var(--brand-gradient);
    display: flex; align-items: center; justify-content: center;
  }
  .tagline {
    color: var(--white); font-size: 21px; font-weight: 400;
    padding-left: 30px;
  }

  /* Front side */
  .card--front {
    left: 214px; top: 463px; width: 648px; height: 351px;
    border: 1px solid var(--frame-cyan);
  }
  .logo-panel { position: absolute; left: 0; top: 0; width: 318px; height: 100%; }
  .logo-panel .brand-square {
    position: absolute; left: 78px; top: 67px; width: 166px; height: 166px; border-radius: 22px;
  }
  .logo-panel .brand-name {
    position: absolute; left: 66px; top: 238px; width: 190px; text-align: center;
    font-size: 45px; font-weight: 700; color: var(--navy); line-height: 1;
    letter-spacing: 2px; white-space: nowrap;
  }
  .website {
    position: absolute; left: 0; top: 320px; width: 308px; text-align: center;
    font-size: 13px; color: var(--cyan); white-space: nowrap;
  }
  .contact-panel {
    position: absolute; left: 318px; top: 0; width: 330px; height: 100%;
    background: var(--brand-gradient); color: var(--white);
  }
  .contact-panel > * { position: absolute; left: 89px; white-space: nowrap; }
  .person-name { top: 53px; font-size: 24px; font-weight: 400; }
  .person-role { top: 94px; font-size: 17px; }
  .address { top: 159px; font-size: 15px; line-height: 23px; }
  .contact-lines { top: 229px; font-size: 15px; line-height: 24px; list-style: none; }
</style>
</head>
<body>
<main class="canvas">

  <section class="card card--back" aria-label="Card back">
    <div class="brand">
      <div class="brand-square"></div>
      <span class="brand-name">ZAVRIQ</span>
    </div>
    <div class="tagline-band">
      <p class="tagline">IT Team Professional</p>
    </div>
  </section>

  <section class="card card--front" aria-label="Card front">
    <div class="logo-panel">
      <div class="brand-square"></div>
      <span class="brand-name">ZAVRIQ</span>
      <p class="website">www.zavriq-demo.com</p>
    </div>
    <div class="contact-panel">
      <h1 class="person-name">Mr. Someone</h1>
      <p class="person-role">Director</p>
      <p class="address">address somewhere<br>Brazil</p>
      <ul class="contact-lines">
        <li>tel:&nbsp;&nbsp; 1-555-787-9090</li>
        <li>cell: 1-555-000-9090</li>
        <li>information@zavriq-demo.com</li>
      </ul>
    </div>
  </section>

</main>
</body>
</html>
```